Brisk Telecom Branding and Visual Identity Project

We need some visual identity items for Brisk Telecom, which should be produced based on the company's logo attached.

I would like the brochure to be as lightweight as possible so that it can be sent via email.

Below are the items we need to be made.

- Company letterhead
- Company brochure in PDF format (single page)
- Email signature (only one)
- Wallpaper
- Banner for use on social media
- Customized shirt

Target Market(s)

Passengers and crew members of ships

Industry/Entity Type

Telecom & Maritime

Colors
0054AA
0677BA
7BADD7
CADEEF
E8F1F8

Requirements
Nice to have
• Colors that match the logo
Should not have
• Colors that clash with the logo colors

```html
<!DOCTYPE html>
<html lang="en">
<head>
<meta charset="utf-8">
<title>Brisk Telecom — Identity Set</title>
<link rel="stylesheet" href="https://fonts.googleapis.com/css2?family=Montserrat:ital,wght@0,400;0,500;0,600;0,700;0,800;0,900;1,600&display=swap">
<style>
:root{
  --blue:#0b6fbd;
  --blue-deep:#0054AA;
  --blue-mid:#0677BA;
  --blue-soft:#7BADD7;
  --blue-pale:#CADEEF;
  --blue-mist:#E8F1F8;
  --grey:#a9a9a9;
  --ink:#3a3a3a;
  --text:#6f6f6f;
  --stage:#e4e5e7;
  --paper:#ffffff;
  --night:#151515;
}
*{box-sizing:border-box;margin:0;padding:0}
html,body{width:1200px;height:967px;overflow:hidden;background:var(--stage)}
body{font-family:'Montserrat',sans-serif;color:var(--ink)}
.canvas{position:relative;width:1200px;height:967px;overflow:hidden;background:var(--stage)}
.item-label{position:absolute;font-size:10px;font-weight:500;color:#8a8a8a}
.sheet{position:absolute;background:var(--paper);box-shadow:0 3px 8px rgba(0,0,0,.18);overflow:hidden}
.abs{position:absolute}

/* brand wordmark */
.brand{position:absolute;display:flex;align-items:center;gap:4px;font-weight:700;color:var(--blue);white-space:nowrap;line-height:1}
.brand .mark{display:inline-block;background:currentColor;border-radius:2px}
.brand.on-dark{color:#fff}

/* business cards */
.card-front .info{position:absolute;right:18px;top:25px;text-align:right;font-size:4.3px;line-height:9px;color:var(--text)}
.card-front .info i,.signature .info i{display:inline-block;width:5px;height:5px;background:var(--blue);border-radius:1px;vertical-align:middle;margin-left:2px}
.card-front .bubble{position:absolute;left:88px;top:12px;width:106px;height:75px;border:3px solid #efefef;border-radius:16px}
.card-front .band{position:absolute;left:0;top:74px;width:120px;height:20px;background:var(--blue);clip-path:polygon(0 0,88% 0,100% 100%,0 100%)}
.card-front .band b{position:absolute;left:13px;top:4px;font-size:6px;color:#fff;font-weight:700}
.card-front .band span{position:absolute;left:13px;top:12px;font-size:4.3px;color:#fff}
.card-back{background:var(--night)}

/* email signature */
.signature .band{position:absolute;left:0;top:20px;width:88px;height:58px;background:var(--blue)}
.signature .bubble{position:absolute;left:66px;top:19px;width:133px;height:51px;background:#fff;border:3px solid #eeeeee;border-radius:14px}
.signature .who{position:absolute;left:72px;top:41px;width:62px;text-align:right;line-height:1.15}
.signature .who b{display:block;font-size:4.6px;color:var(--blue);font-weight:700;white-space:nowrap}
.signature .who span{font-size:3.6px;color:var(--text)}
.signature .info{position:absolute;left:137px;top:29px;font-size:3px;line-height:5.8px;color:var(--text);white-space:nowrap}
.signature .info i{width:4px;height:4px;margin:0 2px 0 0}

/* banner */
.banner .t1{position:absolute;left:25px;top:18px;font-size:33px;font-weight:500;color:var(--grey);line-height:1}
.banner .t2{position:absolute;left:24px;top:52px;font-size:40px;font-weight:900;color:var(--blue);line-height:1}
.banner .t3{position:absolute;left:24px;top:97px;font-size:39px;font-weight:900;color:var(--grey);line-height:1;letter-spacing:-.4px}
.banner .lede{position:absolute;left:25px;top:146px;width:330px;font-size:8.2px;line-height:9.5px;color:var(--text)}
.dots{position:absolute;display:grid;gap:7px}
.dots span{width:2.2px;height:2.2px;border-radius:50%;background:#b7b7b7}
.dots.blue span{background:var(--blue)}
.banner .call{position:absolute;left:58px;top:205px;font-size:8px;font-weight:600;color:var(--ink)}
.banner .call b{display:block;font-size:16px;font-weight:700;color:var(--ink);margin-top:1px}
.social{position:absolute;left:199px;top:202px;display:flex;gap:10px}
.social span{width:17px;height:17px;border-radius:50%;background:var(--blue)}
.banner .web{position:absolute;left:199px;top:223px;font-size:7px;font-weight:700;color:#444}
.btn{position:absolute;left:319px;top:204px;width:80px;height:26px;border-radius:4px;background:var(--blue);color:#fff;font-size:9px;font-weight:700;display:flex;align-items:center;justify-content:center;gap:4px}

/* wallpaper */
.wallpaper{position:absolute;left:98px;top:398px;width:130px;height:185px;background:var(--blue);border-radius:3px;box-shadow:0 3px 8px rgba(0,0,0,.2)}

/* letterhead */
.letterhead .sender{position:absolute;left:25px;top:130px}
.letterhead .sender h2{font-size:12px;font-weight:700;color:var(--blue);margin-bottom:6px}
.letterhead .sender p{font-size:7px;color:var(--text);line-height:12.5px}
.letterhead .date{position:absolute;right:25px;top:188px;font-size:8px;font-weight:500;color:var(--text)}
.letterhead .body{position:absolute;left:25px;width:345px;font-size:8.6px;line-height:12.4px;color:var(--text);text-align:justify}
.letterhead .signer{position:absolute;left:26px;top:392px;font-size:9.4px;font-weight:600;color:var(--ink)}
.letterhead .sign-space{position:absolute;left:40px;top:410px;width:62px;height:38px;background:linear-gradient(90deg,#f4f4f4,#fafafa);border-radius:2px}
.letterhead .foot{position:absolute;left:0;top:520px;width:300px;height:13px;background:var(--blue);font-size:6px;letter-spacing:.8px;color:#fff;padding:3px 0 0 25px}
.letterhead .contact{position:absolute;left:287px;top:469px;width:120px;height:60px;background:#fff;border:3px solid #eeeeee;border-radius:16px}
.letterhead .contact p{position:absolute;right:16px;font-size:5.5px;color:var(--text);display:flex;gap:3px;align-items:center;white-space:nowrap}
.letterhead .contact i{display:inline-block;width:7px;height:7px;background:var(--blue);border-radius:1px}

/* brochure */
.brochure .h-grey{position:absolute;left:17px;font-weight:500;color:var(--grey);line-height:1}
.brochure .h-blue{position:absolute;left:17px;font-weight:900;color:var(--blue);line-height:1}
.brochure .people{position:absolute;left:0;top:170px;width:164px;height:77px;background:var(--blue)}
.brochure .people span{position:absolute;left:17px;top:7px;font-size:29px;font-weight:900;color:#fff;line-height:34px}
.brochure .block{position:absolute;left:18px;width:178px;border-left:1px solid #cfcfcf;padding-left:8px}
.brochure .block h4{font-size:8px;font-weight:500;color:var(--ink)}
.brochure .block h4 b{color:var(--blue);font-weight:700}
.brochure .block p{font-size:5.2px;line-height:6.7px;color:var(--text);text-align:justify}
.brochure .what{position:absolute;left:20px;top:412px;width:172px}
.brochure .what h3{font-size:21px;font-weight:900;color:var(--blue);line-height:1}
.brochure .what h5{font-size:10px;font-weight:600;color:var(--ink);margin:4px 0 11px}
.brochure .what p{font-size:6.2px;line-height:7px;color:var(--text);text-align:justify;margin-bottom:8px}
.services{position:absolute;left:216px;top:320px;width:165px}
.services h3{font-size:21px;font-weight:900;color:var(--ink);line-height:1}
.services h3 b{color:var(--blue)}
.services h5{font-size:11px;font-style:italic;font-weight:600;color:var(--ink);margin-top:4px}
.service{position:absolute;left:216px;width:165px}
.service .ico{position:absolute;left:0;top:-3px;width:29px;height:29px;border-radius:50%;background:var(--blue)}
.service h6{position:absolute;left:40px;top:0;font-size:6.5px;letter-spacing:2.3px;font-weight:700;color:var(--blue)}
.service p{position:absolute;left:40px;top:10px;width:127px;font-size:5.3px;line-height:6.2px;color:var(--text);text-align:justify}
.brochure .foot{position:absolute;left:0;top:520px;width:394px;height:15px;background:var(--blue);display:flex;justify-content:center;gap:14px;align-items:center;font-size:7.8px;color:#fff}
.brochure .foot i{display:inline-block;width:6px;height:6px;background:#fff;border-radius:1px;margin-right:3px;vertical-align:middle}
</style>
</head>
<body>
<main class="canvas">

  <!-- Labels -->
  <div class="item-label" style="left:60px;top:39px">Bcard Front</div>
  <div class="item-label" style="left:265px;top:39px">Bcard Back</div>
  <div class="item-label" style="left:477px;top:39px">Social Media Banner</div>
  <div class="item-label" style="left:57px;top:192px">Email Signature</div>
  <div class="item-label" style="left:141px;top:336px">Wallpaper</div>
  <div class="item-label" style="left:309px;top:336px">Letterhead</div>
  <div class="item-label" style="left:749px;top:336px">Brochure</div>
  <div class="item-label" style="left:125px;top:642px">Customized Shirt</div>

  <!-- Business card front -->
  <section class="sheet card-front" style="left:60px;top:57px;width:186px;height:112px">
    <div class="brand" style="left:12px;top:27px;font-size:7.5px"><span class="mark" style="width:6px;height:6px"></span>Brisk Telecom</div>
    <div class="bubble"></div>
    <div class="info">
      712 Harbor Point Avenue <i></i><br>
      Portsmouth, VA 23704 <br>
      +00 555 210 44 <i></i><br>
      contact@brisktel.com <i></i><br>
      www.brisktel.com <i></i>
    </div>
    <div class="band"><b>DANIEL K. MARLOW</b><span>Managing Director</span></div>
  </section>

  <!-- Business card back -->
  <section class="sheet card-back" style="left:265px;top:57px;width:186px;height:112px">
    <div class="brand" style="left:48px;top:50px;font-size:11px;color:var(--blue)"><span class="mark" style="width:9px;height:9px"></span>Brisk Telecom</div>
  </section>

  <!-- Email signature -->
  <section class="sheet signature" style="left:57px;top:211px;width:394px;height:100px">
    <div class="band"></div>
    <div class="brand on-dark" style="left:7px;top:45px;font-size:6px;gap:3px"><span class="mark" style="width:5px;height:5px"></span>Brisk Telecom</div>
    <div class="bubble"></div>
    <div class="who"><b>DANIEL K. MARLOW</b><span>Managing Director</span></div>
    <div class="info">
      <i></i>712 Harbor Point Avenue<br>
      <span style="padding-left:6px">Portsmouth, VA 23704</span><br>
      <i></i>+00 555 210 44<br>
      <i></i>contact@brisktel.com<br>
      <i></i>www.brisktel.com
    </div>
  </section>

  <!-- Social media banner -->
  <section class="sheet banner" style="left:477px;top:57px;width:667px;height:253px">
    <div class="t1">Creative</div>
    <div class="t2">Brands For</div>
    <div class="t3">Creative People.</div>
    <p class="lede">Lorem ipsum dolor sit amet, consectetuer adipiscing elit, sed diam nonummy nibh euismod tincidunt. Lorem ipsum dolor sit amet.</p>
    <div class="dots" style="left:333px;top:20px;grid-template-columns:repeat(4,2.2px);gap:13px 10px">
      <span></span><span></span><span></span><span></span><span></span><span></span><span></span><span></span>
      <span></span><span></span><span></span><span></span><span></span><span></span><span></span><span></span>
    </div>
    <div class="dots blue" style="left:122px;top:178px;grid-template-columns:repeat(5,2.2px);gap:5px 6px">
      <span></span><span></span><span></span><span></span><span></span><span></span><span></span><span></span><span></span><span></span>
    </div>
    <svg class="abs" style="left:25px;top:206px" width="27" height="22" viewBox="0 0 27 22" aria-hidden="true">
      <path d="M2 8 Q13 -2 25 8 L22 11 Q13 5 5 11 Z" fill="var(--blue)"/>
      <path d="M6 10 H21 L24 21 H3 Z" fill="var(--blue)"/>
      <g fill="#fff"><rect x="10" y="13" width="2" height="2"/><rect x="13" y="13" width="2" height="2"/><rect x="16" y="13" width="2" height="2"/><rect x="10" y="16" width="2" height="2"/><rect x="13" y="16" width="2" height="2"/><rect x="16" y="16" width="2" height="2"/></g>
    </svg>
    <div class="call">Call to find out more<b>+ 0155302418</b></div>
    <div class="social"><span></span><span></span><span></span></div>
    <div class="web">www.brisktel.net</div>
    <div class="btn">Get Started
      <svg width="7" height="8" viewBox="0 0 7 8" aria-hidden="true"><path d="M0 0 L7 4 L0 8 Z" fill="#fff"/></svg>
    </div>
    <svg class="abs" style="left:0;top:0" width="667" height="253" viewBox="0 0 667 253">
      <defs>
        <linearGradient id="cityBanner" x1="0" y1="0" x2="0" y2="1">
          <stop offset="0" stop-color="#8f93c6"/>
          <stop offset=".35" stop-color="#6d7894"/>
          <stop offset=".55" stop-color="#415c3c"/>
          <stop offset=".7" stop-color="#5f6f8e"/>
          <stop offset="1" stop-color="#6e82c4"/>
        </linearGradient>
      </defs>
      <path d="M405 0 V150 Q405 178 436 180 L486 181 L513 232 L510 182 L667 182" fill="none" stroke="var(--blue)" stroke-width="9" stroke-linejoin="round"/>
      <path d="M418 0 V145 Q418 166 440 166 L667 166 V0 Z" fill="url(#cityBanner)" role="img" aria-label="Photo of a waterfront city skyline reflected in a lake"/>
    </svg>
    <div class="brand" style="left:565px;top:213px;font-size:10px"><span class="mark" style="width:8px;height:8px"></span>Brisk Telecom</div>
  </section>

  <!-- Wallpaper -->
  <section class="wallpaper">
    <div class="brand on-dark" style="left:18px;top:86px;font-size:11px"><span class="mark" style="width:9px;height:9px"></span>Brisk Telecom</div>
  </section>

  <!-- Customized shirt -->
  <svg class="abs" style="left:67px;top:663px" width="190" height="245" viewBox="0 0 190 245" aria-label="Polo shirt with brand wordmark">
    <path d="M65 8 L20 30 L0 110 L30 118 L38 80 L36 238 Q95 248 158 238 L152 80 L162 118 L190 110 L170 30 L125 8 Q95 22 65 8 Z" fill="#f6f6f6" stroke="#dedede"/>
    <path d="M65 0 Q95 14 125 0 L133 22 Q112 30 100 40 L95 30 L90 40 Q78 30 57 22 Z" fill="var(--blue)"/>
    <rect x="90" y="32" width="11" height="52" fill="var(--blue)"/>
    <circle cx="95.5" cy="48" r="2" fill="#fff"/><circle cx="95.5" cy="60" r="2" fill="#fff"/><circle cx="95.5" cy="72" r="2" fill="#fff"/>
  </svg>
  <div class="brand" style="left:112px;top:765px;font-size:10px"><span class="mark" style="width:8px;height:8px"></span>Brisk Telecom</div>

  <!-- Letterhead -->
  <section class="sheet letterhead" style="left:309px;top:357px;width:394px;height:553px">
    <div class="brand" style="left:25px;top:40px;font-size:15px"><span class="mark" style="width:12px;height:12px"></span>Brisk Telecom</div>
    <div class="sender">
      <h2>Nora Fielding</h2>
      <p>0155-302-418<br>nora@brisktel.com<br>58 Quayside Ln. Suite 4<br><span style="display:block;margin-top:-3px">Norfolk, VA 23510</span></p>
    </div>
    <div class="date">12 December, 2024</div>
    <p class="body" style="top:210px">Lorem ipsum dolor sit amet, consectetuer adipiscing elit, sed diam nonummy nibh euismod tincidunt ut laoreet dolore magna aliquam erat volutpat. Ut wisi enim ad minim veniam, quis nostrud exerci tation ullamcorper suscipit lobortis nisl ut aliquip ex ea commodo consequat. Duis autem vel eum iriure dolor in hendrerit in vulputate velit esse molestie consequat, vel illum dolore eu feugiat nulla facilisis at vero eros et accumsan et iusto odio dignissim qui blandit praesent luptatum zzril delenit augue duis dolore te feugait nulla facilisi.</p>
    <p class="body" style="top:309px">Lorem ipsum dolor sit amet, cons ectetuer adipiscing elit, sed diam nonummy nibh euismod tincidunt ut laoreet dolore magna aliquam erat volutpat. Ut wisi enim ad minim veniam, quis nostrud exerci tation ullamcorper suscipit lobortis nisl ut aliquip ex ea commodo consequat.</p>
    <div class="signer">Mr. Daniel K. Marlow</div>
    <div class="sign-space" role="img" aria-label="Space for handwritten signature"></div>
    <div class="foot">712 Harbor Point Avenue Portsmouth, VA 23704</div>
    <div class="contact">
      <p style="top:10px">+00 555 210 44 <i></i></p>
      <p style="top:22px">contact@brisktel.com <i></i></p>
      <p style="top:34px">www.brisktel.com <i></i></p>
    </div>
  </section>

  <!-- Brochure -->
  <section class="sheet brochure" style="left:749px;top:357px;width:394px;height:553px">
    <div class="brand" style="left:22px;top:30px;font-size:13px"><span class="mark" style="width:10px;height:10px"></span>Brisk Telecom</div>
    <div class="h-grey" style="top:74px;font-size:23px">Creative</div>
    <div class="h-blue" style="top:101px;font-size:31px">Brands</div>
    <div class="h-grey" style="top:136px;font-size:31px;font-weight:900">For</div>
    <div class="people"><span>Creative<br>People.</span></div>
    <svg class="abs" style="left:0;top:0" width="394" height="320" viewBox="0 0 394 320">
      <defs>
        <linearGradient id="cityBrochure" x1="0" y1="0" x2="0" y2="1">
          <stop offset="0" stop-color="#9a9ccb"/>
          <stop offset=".35" stop-color="#6c7592"/>
          <stop offset=".55" stop-color="#3f5b3c"/>
          <stop offset=".7" stop-color="#5e6f8f"/>
          <stop offset="1" stop-color="#6c82c6"/>
        </linearGradient>
      </defs>
      <path d="M394 32 H195 Q174 32 174 55 V205 Q174 240 205 240 L245 240 L283 302 L290 240 L394 240" fill="none" stroke="var(--blue)" stroke-width="9" stroke-linejoin="round"/>
      <path d="M200 47 H394 V237 H210 Q187 237 187 215 V60 Q187 47 200 47 Z" fill="url(#cityBrochure)" role="img" aria-label="Photo of a waterfront city skyline reflected in a lake"/>
    </svg>
    <div class="block" style="top:262px">
      <h4>ABOUT <b>US</b></h4>
      <p>Lorem Ipsum is simply dummy text of the printing and typesetting industry. Lorem Ipsum has been the industry's standard dummy text ever since the 1500s, when an unknown printer took a galley of type and scrambled it to make a type specimen book. It has survived not only five centuries, but also the leap into electronic typesetting, remaining essentially unchanged.</p>
    </div>
    <div class="block" style="top:336px">
      <h4>OUT <b>TARGET</b></h4>
      <p>Lorem Ipsum is simply dummy text of the printing and typesetting industry. Lorem Ipsum has been the industry's standard dummy text ever since the 1500s, when an unknown printer took a galley of type and scrambled it to make a type specimen book. It has survived not only five centuries, but also the leap into electronic typesetting, remaining essentially unchanged.</p>
    </div>
    <div class="what">
      <h3>What we do.</h3>
      <h5>Here’s how we can help</h5>
      <p>Lorem ipsum dolor sit amet, consectetuer adipiscing elit, sed diam nonummy nibh euismod tincidunt. Lorem ipsum dolor sit amet.</p>
      <p>consectetuer adipiscing elit,sed diam nonummy nibh euismod tinciduLorem ipsum dolor sit</p>
    </div>
    <div class="services">
      <h3>Our <b>Services</b></h3>
      <h5>Here’s how we can help</h5>
    </div>
    <div class="service" style="top:380px">
      <span class="ico"></span>
      <svg class="abs" style="left:7px;top:4px" width="15" height="15" viewBox="0 0 15 15" aria-hidden="true"><path d="M1 6 L14 2 L9 13 L7 8 Z" fill="none" stroke="#fff" stroke-width="1"/></svg>
      <h6>HEADLINE 01</h6>
      <p>Lorem ipsum dolor sit amet, consectetur adipiscing elit. Nulla eget mollis enim. In odio felis, egestas ut dapibus vitae, laoreet ut nisl.</p>
    </div>
    <div class="service" style="top:428px">
      <span class="ico"></span>
      <svg class="abs" style="left:7px;top:4px" width="15" height="15" viewBox="0 0 15 15" aria-hidden="true"><g fill="none" stroke="#fff" stroke-width="1"><rect x="2" y="8" width="2.5" height="5"/><rect x="6" y="6" width="2.5" height="7"/><rect x="10" y="4" width="2.5" height="9"/><path d="M1 13.5 H14"/></g></svg>
      <h6>HEADLINE 02</h6>
      <p>Lorem ipsum dolor sit amet, consectetur adipiscing elit. Nulla eget mollis enim. In odio felis, egestas ut dapibus vitae, laoreet ut nisl.</p>
    </div>
    <div class="service" style="top:475px">
      <span class="ico"></span>
      <svg class="abs" style="left:7px;top:4px" width="15" height="15" viewBox="0 0 15 15" aria-hidden="true"><g fill="none" stroke="#fff" stroke-width="1"><circle cx="7.5" cy="7.5" r="6"/><ellipse cx="7.5" cy="7.5" rx="2.6" ry="6"/><path d="M1.5 7.5 H13.5 M2.5 4.5 H12.5 M2.5 10.5 H12.5"/></g></svg>
      <h6>HEADLINE 03</h6>
      <p>Lorem ipsum dolor sit amet, consectetur adipiscing elit. Nulla eget mollis enim. In odio felis, egestas ut dapibus vitae, laoreet ut nisl.</p>
    </div>
    <div class="foot">
      <span><i></i>+00 555 210 44</span>
      <span><i></i>contact@brisktel.com</span>
      <span><i></i>www.brisktel.com</span>
    </div>
  </section>

</main>
</body>
</html>
```